Race car follow-up website needs web design

We are currently finalising a website which allows amateur and professional owners of race cars to track the running time of the car and all installed parts (drive shafts, gearbox etc.). The site is working for a technical point of view, but needs a nice design applied to it.

The website is made with Bootstrap 3.x and does not need a mobile skin. We target desktop and tablet users. This means that the delivered work should be easy to incorporate in the Bootstrap site that currently exists, from a technical point of view.

In attachment you can find all the screens that need skinning. If you think some stuff can be done better from a usability or design point of view (size of tables, placement of buttons etc.), do not hesitate to make a suggestion. We are open to positive criticism, and the current "base" design is not carved in stone. The colors currently used are basic Bootstrap so that can change too. There are no limits whatsoever, as long as the result looks good.

We have a big amount of racing/racecar/mechanic/pitbox related photo material that can be used, so do not hesitate to ask for material if needed.

The start page should be something along the lines of these sites:

https://plovik.example/
http://quandrel.example/
https://torvane.example/
http://www.brismel.example/

Or in words: a top navigation bar (as seen in the screenshots). A full-width image relevant to the content (racing related) with some text in overlay (A sort of slogan along the lines of "Let us track your parts" or "Parts tracking for you race or trackday car" ). Under that image there should then be a very high-level overview of what the website can be used for (In a few steps, with graphics/photos, schematics, showing driving the car, data transfer, management in the site.). This so the potential user can quickly see if it is of any interest to him/her.

Basically:

Drive --- Download data -- Get Alerted

each step should contain an "icon" representing what it is about, and a few lines of text explaining what is meant.

On that page (in the image part, or below the explanation) there should be 2 links (buttons). One leads to the pricing page, one to the registration page.

Of course this first page cannot be finalised until we give the complete details of the content, so please provide a high-level design and the person I work with will receive the detailed specs (the text for the different steps etc).

The other screens are (we think) self-explanatory. Please look at them in chronological order (they are prefixed 00 to 19)

There are screenshots of the manual. This page will also need to be styled (to match the rest of the site and to make the layout a bit more sexy). We will of course provide the original html file to this once the content needs to be finalised.

Besides the website, a mail template is required too. The site sends mails for:
- registration confirmation
- lost password
- alerts related to the car parts or the data files.

These mails should also have a professional looking skin (right now they are plain text)

Just to make things clear, if you think the base design we made is "crap", please suggest improvements (for instance, menu placement in the bottom, positioning of certain elements, tables that might be better off somewhere else, the car details on top that take too much screen real-estate etc. etc.). This site has been built by developers, not by designers. The only condition is that it should be technically possible in a reasonable amount of time using Bootstrap 3.x

Please provide the resources in such a way that a developer with web skills can directly implement them. So any slicing of graphics should be done by the designer. If you only provide us a good looking psd file we won't be able to do anything with that, unfortunately.

If you, as a designer, have a passion for sports cars, race cars, trackdays and/or GT car racing, this is of course a plus. The collaboration will be a lot easier if we speak the same "language".

Please provide at least a design of
- the start page
- the "car details" page
- one of the list modals
- one of the form modals

so we can at least know how the rest of the pages will look

The name is Pitlane Ledger.

Some pictures that can be used:

https://www.snapvale.example/photos/58013274@K02/31720958316/
https://www.snapvale.example/photos/58013274@K02/4821093765/
https://www.snapvale.example/photos/58013274@K02/4819372610/
https://www.snapvale.example/photos/58013274@K02/4806215937/
https://www.snapvale.example/photos/58013274@K02/4763910528/
https://www.snapvale.example/photos/58013274@K02/4702836419/
https://www.snapvale.example/photos/58013274@K02/4591027364/
https://www.snapvale.example/photos/58013274@K02/4370918254/
https://www.snapvale.example/photos/58013274@K02/3960281547/
https://www.snapvale.example/photos/58013274@K02/3927048163/
https://www.snapvale.example/photos/58013274@K02/3912705836/
https://www.snapvale.example/photos/58013274@K02/3912708291/
https://www.snapvale.example/photos/58013274@K02/3890461725/
https://www.snapvale.example/photos/58013274@K02/3881937042/
https://www.snapvale.example/photos/58013274@K02/3881940658/
https://www.snapvale.example/photos/58013274@K02/2170395846/
https://www.snapvale.example/photos/58013274@K02/1408275963/
https://www.snapvale.example/photos/58013274@K02/1496083712/
https://www.snapvale.example/photos/58013274@K02/1327540968/
https://www.snapvale.example/photos/58013274@K02/1327546019/

Basically you take whatever you want from this guy’s photo stream:
https://www.snapvale.example/photos/58013274@K02/

I know him personally so there should be no copyright issues.

Most users of the site will run so called "GT" cars (Porsche, Ferrari etc.), so please refrain from using (or referencing) open wheelers, F1, LMP etc.

There is a logo contest too: http://gigs.artmosaic.example/gig.aspx?id=730418

I just updated the brief with some more info and images you can use.

I have updated the brief. This is added: for the first screen, the schematics are explained in a bit more detail: Basically: Drive ---> Download data --> Get Alerted each step should contain an "icon" representing what it is about, and a few lines of text explaining what is meant.

Dear designers, As we have received numerous remarks about our contest from you and your colleagues we have contacted ArtMosaic to solve the situation. This contest will be split into two different contests. One logo design contest for $400 and one website design contest for the $1480. Everyone who has submitted logos can of course participate with those logos in the logo design contest (there are a few that we like, which have been submitted). We are very sorry for the inconvenience we might have caused, and if you want to redraw your designs already submitted because of this we will fully understand this, but we hope this decision will make things clearer for everyone participating. As soon as matters are changed we will send you all a new message with the updated information. Thanks for your understanding. Kelvor BVBA

The logo contest has been created: http://gigs.artmosaic.example/gig.aspx?id=730418

Reason: Because of the split in webdesign / logo the deadline has been extended so non-logo webdesigners can participate too. Logo project: http://gigs.artmosaic.example/gig.aspx?id=730418

The pricing page has been added in the screenshots section

Trackday enthousiasts, race car owners, race teams.

• No video
No huge "footer" with a lot of links to navigate the site, since there will be very litte content.
No references to non-GT type cars (so no F1, no Formula Renault, no LMP1/LMP2) or street cars.

```html
<!DOCTYPE html>
<html lang="en">
<head>
<meta charset="utf-8">
<title>Pitlane Ledger</title>
<link rel="stylesheet" href="https://fonts.googleapis.com/css2?family=Open+Sans:wght@400;600;700&family=Varela+Round&display=swap">
<style>
  :root {
    --brand-red: #b80000;
    --brand-red-dark: #9a0000;
    --ink: #222222;
    --ink-soft: #555555;
    --nav-ink: #555555;
    --tab-grey: #e6e6e6;
    --header-bg: #fbfbfb;
    --hero-dark: #3a3b3d;
    --hero-mid: #8d8e90;
    --hero-light: #b9babb;
    --footer-bg: #1c1c1c;
    --footer-ink: #b5b5b5;
    --subscribe: #e8431a;
    --white: #ffffff;
  }
  * { box-sizing: border-box; margin: 0; padding: 0; }
  html, body { width: 1151px; height: 1200px; overflow: hidden; }
  body {
    position: relative;
    background: var(--white);
    font-family: "Open Sans", Arial, sans-serif;
    color: var(--ink);
  }

  /* Header */
  .site-header {
    position: absolute; left: 0; top: 0; width: 1151px; height: 102px;
    background: linear-gradient(#ffffff, var(--header-bg) 60%, #f1f1f1);
    border-bottom: 2px solid var(--brand-red);
  }
  .account-tab {
    position: absolute; left: 652px; top: 0; width: 403px; height: 39px;
    background: linear-gradient(#f4f4f4, var(--tab-grey));
    border-radius: 0 0 22px 22px;
  }
  .account-tab .picker {
    position: absolute; top: 10px; font-size: 13.5px; color: #8a8a8a;
  }
  .account-tab .picker::after {
    content: ""; display: inline-block; margin-left: 6px; vertical-align: 2px;
    border-left: 5px solid transparent; border-right: 5px solid transparent;
    border-top: 6px solid #a8a8a8;
  }
  .picker.car { left: 22px; }
  .picker.user { left: 215px; }
  .logout {
    position: absolute; left: 298px; top: 3px; width: 70px; height: 32px;
    background: var(--brand-red); color: var(--white); border-radius: 2px;
    font-size: 13.5px; font-weight: 600; line-height: 32px; text-align: center;
  }
  .brand {
    position: absolute; left: 107px; top: 30px; display: flex; align-items: center; gap: 22px;
  }
  .brand-dot { width: 64px; height: 64px; border-radius: 50%; background: var(--brand-red); }
  .brand-name {
    font-family: "Varela Round", "Open Sans", sans-serif; font-size: 34px; color: #3c3c3c;
  }
  .main-nav { position: absolute; top: 77px; left: 0; }
  .main-nav a {
    position: absolute; white-space: nowrap; text-decoration: none;
    font-size: 13.5px; color: var(--nav-ink);
  }
  .main-nav a.active { color: var(--brand-red); }

  /* Hero */
  .hero {
    position: absolute; left: 0; top: 102px; width: 1151px; height: 499px;
    background:
      radial-gradient(ellipse 420px 220px at 430px 280px, var(--hero-dark) 0%, #4c4d50 55%, rgba(90,91,94,0) 100%),
      linear-gradient(180deg, var(--hero-light) 0%, var(--hero-mid) 60%, #6f7072 100%);
    box-shadow: 0 6px 8px -4px rgba(0,0,0,0.35);
  }
  .hero-arrow {
    position: absolute; top: 258px; width: 42px; height: 42px; border-radius: 50%;
    background: var(--white); border: 3px solid #9c9c9c;
  }
  .hero-arrow svg { position: absolute; left: 10px; top: 10px; }
  .hero-arrow.prev { left: 24px; }
  .hero-arrow.next { left: 1071px; }
  .hero-title {
    position: absolute; left: 683px; top: 316px; font-size: 42px; font-weight: 700;
    color: var(--white); letter-spacing: 0.5px; text-shadow: 0 0 3px #000, 1px 2px 3px #000;
    white-space: nowrap; line-height: 1;
  }
  .hero-quote {
    position: absolute; left: 685px; top: 378px; width: 360px;
    font-size: 15.5px; line-height: 23px; color: var(--white);
    text-shadow: 0 1px 2px rgba(0,0,0,0.8);
  }
  .hero-cta {
    position: absolute; left: 687px; top: 482px; width: 338px; height: 60px;
    background: rgba(20,20,20,0.8); border: 1px solid #666; border-radius: 3px;
    color: var(--white); font-size: 29px; font-weight: 600; text-align: center; line-height: 58px;
    text-shadow: 0 1px 3px #000;
  }

  /* Features */
  .feature { position: absolute; top: 705px; width: 260px; text-align: center; }
  .feature .icon { height: 32px; display: flex; justify-content: center; align-items: center; }
  .feature h2 { margin-top: 23px; font-size: 19.5px; font-weight: 600; color: var(--ink); }
  .feature p { margin-top: 15px; font-size: 12.5px; line-height: 19.2px; color: var(--ink-soft); padding: 0 13px; }
  .feature .read-more {
    display: inline-block; margin-top: 18px; width: 96px; height: 31px; line-height: 31px;
    background: var(--brand-red); color: var(--white); font-size: 12.5px; border-radius: 2px;
    border-bottom: 2px solid var(--brand-red-dark);
  }
  .feature.running { left: 123px; }
  .feature.installed { left: 443px; }
  .feature.update { left: 760px; }

  /* Footer */
  .site-footer {
    position: absolute; left: 0; top: 1098px; width: 1151px; height: 102px; background: var(--footer-bg);
  }
  .newsletter-title { position: absolute; left: 111px; top: 15px; font-size: 18.5px; color: var(--footer-ink); }
  .newsletter-form {
    position: absolute; left: 111px; top: 50px; width: 218px; height: 30px;
    border: 1px solid #8a8a8a; border-radius: 3px; background: #6a6a6a; overflow: hidden;
  }
  .newsletter-form .email {
    position: absolute; left: 16px; top: 7px; font-size: 11px; font-style: italic; color: #e6e6e6;
  }
  .newsletter-form .subscribe {
    position: absolute; right: 0; top: 0; width: 83px; height: 28px; background: var(--subscribe);
    color: var(--white); font-size: 15px; font-weight: 600; text-align: center; line-height: 28px;
  }
  .copyright { position: absolute; right: 121px; top: 39px; font-size: 12px; color: var(--footer-ink); text-align: right; line-height: 23px; }
</style>
</head>
<body>
  <header class="site-header">
    <div class="account-tab">
      <span class="picker car">Select Car</span>
      <span class="picker user">Jonas</span>
      <span class="logout">LOG OUT</span>
    </div>
    <div class="brand">
      <span class="brand-dot"></span>
      <span class="brand-name">Pitlane Ledger</span>
    </div>
    <nav class="main-nav">
      <a class="active" href="#" style="left:516px">WHO WE ARE</a>
      <a href="#" style="left:640px">WHAT WE DO</a>
      <a href="#" style="left:765px">OUR TEAM</a>
      <a href="#" style="left:872px">BLOG</a>
      <a href="#" style="left:947px">CONTACT US</a>
    </nav>
  </header>

  <section class="hero" role="img" aria-label="Photo of a black GT race car from the rear on a grey race track">
    <span class="hero-arrow prev"><svg width="16" height="16" viewBox="0 0 16 16"><path d="M11 2 L5 8 L11 14" fill="none" stroke="#333" stroke-width="3"/></svg></span>
    <span class="hero-arrow next"><svg width="16" height="16" viewBox="0 0 16 16"><path d="M5 2 L11 8 L5 14" fill="none" stroke="#333" stroke-width="3"/></svg></span>
    <h1 class="hero-title" style="top:214px">TRACK THE PARTS</h1>
    <p class="hero-quote" style="top:276px">"Follow up what distance or running time the different parts of your car have and get notified when it is time to replace them"</p>
    <span class="hero-cta" style="top:380px">SIGN UP FOR FREE!</span>
  </section>

  <section class="feature running">
    <div class="icon">
      <svg width="28" height="28" viewBox="0 0 28 28"><circle cx="14" cy="15" r="10.5" fill="none" stroke="#333" stroke-width="3"/><path d="M14 15 L9 9" stroke="#333" stroke-width="3"/><rect x="11" y="1" width="6" height="3" fill="#333"/></svg>
    </div>
    <h2>Track the Running Time</h2>
    <p>Cras ut porta ipsum. Fusce sapien ante, tristique non cursus in, tincidunt eget felis. Mauris velit dui, vestibulum et urna ac, adipiscing vestibulum dolor. Aenean sed arcu ac quam euismod eleifend in et felis.</p>
    <span class="read-more">READ MORE</span>
  </section>

  <section class="feature installed">
    <div class="icon">
      <svg width="30" height="30" viewBox="0 0 30 30"><g fill="#333"><circle cx="15" cy="15" r="10"/><rect x="12" y="1" width="6" height="28"/><rect x="12" y="1" width="6" height="28" transform="rotate(45 15 15)"/><rect x="12" y="1" width="6" height="28" transform="rotate(90 15 15)"/><rect x="12" y="1" width="6" height="28" transform="rotate(135 15 15)"/></g><circle cx="15" cy="15" r="4" fill="#fff"/></svg>
    </div>
    <h2>Track The Installed Parts</h2>
    <p>Cras ut porta ipsum. Fusce sapien ante, tristique non cursus in, tincidunt eget felis. Mauris velit dui, vestibulum et urna ac, adipiscing vestibulum dolor. Aenean sed arcu ac quam euismod eleifend in et felis.</p>
    <span class="read-more">READ MORE</span>
  </section>

  <section class="feature update">
    <div class="icon">
      <svg width="28" height="28" viewBox="0 0 28 28"><path d="M14 2 L23 11 L18 11 L18 19 L10 19 L10 11 L5 11 Z" fill="#333"/><path d="M3 17 L3 25 L25 25 L25 17" fill="none" stroke="#333" stroke-width="3"/></svg>
    </div>
    <h2>Update Your Car Parts</h2>
    <p>Cras ut porta ipsum. Fusce sapien ante, tristique non cursus in, tincidunt eget felis. Mauris velit dui, vestibulum et urna ac, adipiscing vestibulum dolor. Aenean sed arcu ac quam euismod eleifend in et felis.</p>
    <span class="read-more">READ MORE</span>
  </section>

  <footer class="site-footer">
    <h3 class="newsletter-title">Newsletter</h3>
    <div class="newsletter-form">
      <span class="email">Email</span>
      <span class="subscribe">Subscribe</span>
    </div>
    <p class="copyright">© 2014 Pitlane Ledger, All rights reserved<br>X2</p>
  </footer>
</body>
</html>
```